Brightwell Ledger needs a Business Card

Designers!
More often than not, people want a cheap business card and often argue "I only want 100, not 500" - Years ago I worked in print and always wanted a client to ask for something that challenged me and would be great for my portfolio.

Years have past, and I dont have the time to do it myself so I'd love to see what everyone can offer.

Reason: Hey Guys, The designs are looking good but i've extended it a few more days as I wont be near a laptop and i'm trying to provide everyone feedback - Sorry!

Target Market(s)

Key decision makers, Potential Clients, Networking events and opportunities.

Industry/Entity Type

Business

Requirements
Must have
• Typography is very important. The type of paper is important.
The print, the shape. The creativity.
I'm very inspired by the below link
http://www.pelvarno.com/blog/business-card-design/

Nice to have
• Stencelled cutouts. Embossing, nice typography.
I'd like the business card to be a conversation piece itself.

Attached is an image of business cards i've had in the past.
Additionally, some logos i've recently had designed by MakerFlock.

```html
<!DOCTYPE html>
<html lang="en">
<head>
<meta charset="utf-8">
<title>Brightwell Ledger — Business Card</title>
<link rel="stylesheet" href="https://fonts.googleapis.com/css2?family=Roboto:wght@300;400&display=swap">
<style>
  :root {
    --backdrop: #e9e6e1;
    --card-navy: #0c2c57;
    --card-cream: #eeeadc;
    --ink-light: #ffffff;
    --ink-soft: #c9d3e2;
    --rule: #7d90ad;
  }
  * { margin: 0; padding: 0; box-sizing: border-box; }
  html, body {
    width: 1200px;
    height: 800px;
    overflow: hidden;
    background: var(--backdrop);
    font-family: "Roboto", Arial, sans-serif;
  }
  .canvas {
    position: relative;
    width: 1200px;
    height: 800px;
  }
  .card {
    position: absolute;
    left: 280px;
    width: 640px;
    height: 356px;
    border-radius: 22px;
    box-shadow: 0 6px 18px rgba(0,0,0,0.12);
    overflow: hidden;
  }
  .card--back {
    top: 30px;
    background: var(--card-cream);
  }
  .card--front {
    top: 414px;
    background: var(--card-navy);
    color: var(--ink-light);
  }
  .stencil-cut {
    position: absolute;
    width: 64px;
    height: 64px;
    background: var(--backdrop);
  }
  .card--back .stencil-cut { left: 40px; top: 28px; }
  .card--front .stencil-cut { right: 48px; top: 42px; }

  .brand {
    position: absolute;
    left: 48px;
    top: 206px;
    width: 236px;
  }
  .brand__name {
    display: flex;
    align-items: center;
    gap: 8px;
    font-weight: 300;
    font-size: 15px;
    letter-spacing: 1.6px;
    text-transform: uppercase;
    line-height: 1.1;
    white-space: nowrap;
    color: var(--ink-light);
  }
  .brand__mark {
    width: 12px;
    height: 12px;
    flex: none;
    background: var(--ink-light);
  }
  .brand__web {
    margin-top: 6px;
    padding-top: 4px;
    border-top: 1px solid var(--rule);
    font-weight: 300;
    font-size: 9px;
    letter-spacing: 2.4px;
    white-space: nowrap;
    color: var(--ink-soft);
  }
  .divider {
    position: absolute;
    left: 304px;
    top: 186px;
    width: 1px;
    height: 96px;
    background: var(--rule);
  }
  .contact {
    position: absolute;
    left: 340px;
    top: 232px;
    font-weight: 300;
    font-size: 11px;
    line-height: 1.25;
    white-space: nowrap;
    color: var(--ink-soft);
  }
  .contact__name {
    font-weight: 300;
    font-size: 14px;
    color: var(--ink-light);
    margin-bottom: 2px;
  }
</style>
</head>
<body>
<main class="canvas">
  <section class="card card--back" aria-label="Card back">
    <div class="stencil-cut"></div>
  </section>

  <section class="card card--front" aria-label="Card front">
    <div class="stencil-cut"></div>

    <div class="brand">
      <div class="brand__name"><span class="brand__mark"></span>Brightwell Ledger</div>
      <div class="brand__web">brightwellledger.com.au</div>
    </div>

    <div class="divider"></div>

    <div class="contact">
      <p class="contact__name">NAME SURNAME</p>
      <p>031 742 508</p>
      <p>468 390 127</p>
      <p>www.website.com</p>
      <p>mail@mail.com</p>
    </div>
  </section>
</main>
</body>
</html>
```